An international wholesale business needs letterhead design

Logo file is attached. Please design a letterhead with the following details:

- Company Name and Logo
- Address
- VAT Registration number
- Phone No
- Website address

```html
<!DOCTYPE html>
<html lang="en">
<head>
<meta charset="utf-8">
<title>Norvell Trading Letterhead</title>
<link href="https://fonts.googleapis.com/css2?family=Poppins:wght@400;600;700&display=swap" rel="stylesheet">
<style>
  :root {
    --backdrop: #e7ecec;
    --paper: #ffffff;
    --ink: #111111;
    --brand-red: #d20f0f;
    --brand-grey: #8aa0a6;
    --brand-black: #0e0e0e;
  }
  * { margin: 0; padding: 0; box-sizing: border-box; }
  html, body {
    width: 1200px; height: 1200px; overflow: hidden;
    background: var(--backdrop);
    font-family: "Poppins", sans-serif;
    color: var(--ink);
  }
  .letterhead {
    position: absolute; left: 160px; top: 30px;
    width: 881px; height: 1140px;
    background: var(--paper);
    overflow: hidden;
  }
  .brand {
    position: absolute; left: 77px; top: 128px;
    display: flex; align-items: center; gap: 16px;
  }
  .brand-mark {
    width: 96px; height: 96px; border-radius: 50%;
    background: var(--brand-red);
  }
  .brand-name {
    font-weight: 600; font-size: 44px; letter-spacing: 1px;
    color: var(--brand-red); line-height: 1;
  }
  .salutation {
    position: absolute; left: 77px; top: 316px;
    font-weight: 700; font-size: 19px; line-height: 24px;
  }
  .letter-body {
    position: absolute; left: 92px; top: 374px; width: 738px;
    font-size: 14px; line-height: 17.2px;
    hyphens: auto;
  }
  .letter-body p { margin-bottom: 34px; }
  .contact-bar {
    position: absolute; left: 78px; top: 989px;
    display: flex; align-items: center;
    font-size: 14px; font-weight: 400; white-space: nowrap;
  }
  .contact-item { display: flex; align-items: center; gap: 10px; margin-right: 18px; }
  .contact-item:last-child { margin-right: 0; }
  .contact-item svg { width: 21px; height: 21px; flex: none; }
  .brand-bands {
    position: absolute; left: 0; bottom: 0; width: 100%; height: 19px;
    display: flex;
  }
  .band-grey { width: 293px; background: var(--brand-grey); }
  .band-red { width: 290px; background: var(--brand-red); }
  .band-black { flex: 1; background: var(--brand-black); }
</style>
</head>
<body>
<main class="letterhead">
  <header class="brand">
    <span class="brand-mark"></span>
    <span class="brand-name">NORVELL TRADING</span>
  </header>

  <p class="salutation">Dear Sir,</p>

  <section class="letter-body">
    <p>Lorem Ipsum is simply dummy text of the printing and typesetting industry. Lorem Ipsum has been the industry's standard dummy text ever since the 1500s, when an unknown printer took a galley of type and scrambled it to make a type specimen book. It has survived not only five centuries, but also the leap into electronic typesetting, remaining essentially unchanged. It was popularised in the 1960s with the release of Lettermark sheets containing Lorem Ipsum passages, and more recently with desktop publishing software like Folio PageSetter including versions of Lorem Ipsum.</p>
    <p>It is a long established fact that a reader will be distracted by the readable content of a page when looking at its layout. The point of using Lorem Ipsum is that it has a more-or-less normal distribution of letters, as opposed to using 'Content here, content here', making it look like readable English. Many desktop publishing packages and web page editors now use Lorem Ipsum as their default model text, and a search for 'lorem ipsum' will uncover many web sites still in their infancy. Various versions have evolved over the years, sometimes by accident, sometimes on purpose (injected humour and the like).</p>
    <p>Contrary to popular belief, Lorem Ipsum is not simply random text. It has roots in a piece of classical Latin literature from 45 BC, making it over 2000 years old. Daniel Hartwell, a Latin professor at Westbrook College in Virginia, looked up one of the more obscure Latin words, consectetur, from a Lorem Ipsum passage, and going through the cites of the word in classical literature, discovered the undoubtable source. Lorem Ipsum comes from sections 1.10.32 and 1.10.33 of "de Finibus Bonorum et Malorum" (The Extremes of Good and Evil) by Aurelian, written in 45 BC. This book is a treatise on the theory of ethics, very popular during the Renaissance. The first line of Lorem Ipsum, "Lorem ipsum dolor sit amet..", comes from a line in section 1.10.32.</p>
  </section>

  <footer class="contact-bar">
    <div class="contact-item">
      <svg viewBox="0 0 24 24" fill="none" stroke="#d20f0f" stroke-width="1.4" stroke-linejoin="round"><path d="M5 3l4 1 1.5 4-2.5 1.5a11 11 0 0 0 6.5 6.5L16 13.5l4 1.5 1 4-2 2C10 21 3 14 3 5z"/></svg>
      <span>1234567890</span>
    </div>
    <div class="contact-item">
      <svg viewBox="0 0 24 24" fill="none" stroke="#d20f0f" stroke-width="1.4"><path d="M12 21s-6-6.5-6-11a6 6 0 0 1 12 0c0 4.5-6 11-6 11z"/><circle cx="12" cy="10" r="2.3"/><path d="M7 21h10"/></svg>
      <span>Your Adress here</span>
    </div>
    <div class="contact-item">
      <svg viewBox="0 0 24 24" fill="none" stroke="#d20f0f" stroke-width="1.3"><rect x="5" y="3" width="12" height="17"/><path d="M8 7h6M8 10h6M8 13h4"/><circle cx="17" cy="16" r="3"/></svg>
      <span>VAT Registration number</span>
    </div>
    <div class="contact-item">
      <svg viewBox="0 0 24 24" fill="none" stroke="#d20f0f" stroke-width="1.3"><circle cx="12" cy="12" r="9"/><ellipse cx="12" cy="12" rx="4" ry="9"/><path d="M3 12h18M4.5 7.5h15M4.5 16.5h15"/></svg>
      <span>www.norvelltrading.com</span>
    </div>
  </footer>

  <div class="brand-bands">
    <span class="band-grey"></span>
    <span class="band-red"></span>
    <span class="band-black"></span>
  </div>
</main>
</body>
</html>
```